RTM Global (Rooted Tillage and Meadowcraft) is a company positioning itself as a global leader in regenerative and sustainable agriculture and irrigation technologies and solutions, with a focus on soil health. Please read the attached information (which can be used in the website).
We're looking for a modern website which also compliments the agricultural sector and the natural resources we work with. We want the website to be fairly concise and to the point without elaborating too much. We would rather attract the clients to engage with us rather than drawing their own conclusions from the website.

```html
<!DOCTYPE html>
<html lang="en">
<head>
<meta charset="utf-8">
<title>RTM Global — Rooted Tillage and Meadowcraft</title>
<link href="https://fonts.googleapis.com/css2?family=Lexend:wght@300;400;500;600;700;800&display=swap" rel="stylesheet">
<style>
:root{
  --cream:#f4f3ea;
  --ink:#1f2220;
  --text:#3d3f3a;
  --muted:#5b5d57;
  --blue:#3e5d8f;
  --navy:#2f4778;
  --olive:#6e7f45;
  --olive-dark:#46562a;
  --leaf:#8a9c5c;
  --charcoal:#2c2b27;
  --white:#ffffff;
}
*{margin:0;padding:0;box-sizing:border-box}
html,body{width:1200px;height:4169px;overflow:hidden}
body{
  position:relative;font-family:"Lexend",sans-serif;color:var(--text);
  background:
    radial-gradient(520px 420px at 1100px 200px,rgba(214,226,160,.45),transparent 70%),
    radial-gradient(560px 460px at 120px 1300px,rgba(224,230,170,.45),transparent 70%),
    radial-gradient(520px 420px at 1150px 1500px,rgba(224,230,170,.35),transparent 70%),
    var(--cream);
}
.abs{position:absolute}
.btn{position:absolute;background:var(--blue);color:var(--white);font-size:14px;font-weight:500;
  display:flex;align-items:center;justify-content:center;letter-spacing:.3px;text-transform:uppercase}
.topbar{left:632px;top:0;width:568px;height:33px;background:var(--navy);
  clip-path:polygon(0 0,100% 0,100% 100%,34px 100%);display:flex;align-items:center;
  gap:22px;padding-left:60px;color:var(--white);font-size:13px}
.topbar svg{vertical-align:-3px;margin-right:6px}
.topbar .dots{display:flex;gap:12px;margin-left:6px}
.topbar .dots span{width:11px;height:11px;border-radius:50%;border:1.5px solid var(--white)}
.brand{display:flex;align-items:center;gap:10px}
.brand .mark{width:30px;height:30px;border-radius:50%;background:var(--blue)}
.brand .name{font-size:30px;font-weight:700;color:var(--blue);letter-spacing:-.5px}
.nav{top:52px;left:544px;display:flex;gap:45px;font-size:14px;color:var(--ink)}
.nav .active{color:var(--olive)}
.pill{left:65px;top:170px;width:73px;height:170px;border-radius:37px;border:2px solid #fff;
  background:linear-gradient(180deg,rgba(255,255,255,.8),rgba(255,255,255,.2))}
.avatar{left:70px;top:272px;width:62px;height:62px;border-radius:50%;background:linear-gradient(160deg,#8aa06a,#5a6b3e)}
.hero-t1{left:174px;top:190px;font-size:52px;font-weight:700;color:var(--ink);letter-spacing:.5px}
.hero-t2{left:178px;top:254px;height:57px;padding:0 16px;background:var(--olive);color:var(--white);
  font-size:52px;font-weight:700;line-height:57px;letter-spacing:.5px}
.hero-name{left:66px;top:482px;font-size:42px;font-weight:600;color:var(--ink)}
.hero-sub{left:66px;top:545px;width:330px;font-size:15px;line-height:22px;color:var(--text)}
.eyebrow{font-size:14px;color:var(--muted);text-transform:uppercase}
.h2{font-size:45px;font-weight:600;color:var(--ink);line-height:53px}
.para{font-size:16.5px;line-height:26.7px;color:var(--text);font-weight:300}
.svc{position:absolute;top:1788px;width:333px;height:338px;background:var(--white);
  box-shadow:0 6px 18px rgba(0,0,0,.12);border-radius:4px;text-align:center}
.svc .icon{position:absolute;left:124px;top:-42px;width:84px;height:84px;border-radius:50%;
  background:var(--white);box-shadow:0 3px 10px rgba(0,0,0,.15);display:flex;align-items:center;justify-content:center}
.svc h3{margin-top:66px;font-size:23px;font-weight:400;color:var(--ink);line-height:30px;height:60px;display:flex;align-items:center;justify-content:center}
.svc p{margin:22px 26px 0;font-size:13.5px;line-height:22px;color:var(--muted);font-weight:300;height:90px}
.svc .btn{left:95px;top:255px;width:143px;height:46px}
.chev{position:absolute;width:20px;height:20px}
.why{position:absolute;top:2322px;width:345px;height:380px;background:var(--white);border-radius:4px;
  box-shadow:0 4px 14px rgba(0,0,0,.08);overflow:hidden}
.why h3{position:absolute;left:14px;top:26px;font-size:22px;font-weight:500;color:var(--ink);line-height:28px}
.why .ph{position:absolute;left:0;top:92px;width:345px;height:191px}
.why p{position:absolute;left:14px;top:305px;right:14px;font-size:13.5px;line-height:22px;color:var(--muted);font-weight:300}
.impact-band{left:0;top:2823px;width:1200px;height:560px;background:var(--charcoal)}
.field{position:absolute;border:1px solid rgba(255,255,255,.35);color:rgba(255,255,255,.75);font-size:13px;padding:12px}
.footer{left:97px;top:3843px;width:1006px;height:340px;background:var(--white);border-radius:32px 32px 0 0}
.footer h4{position:absolute;font-size:18px;font-weight:400;color:var(--ink)}
.footer .link{position:absolute;left:461px;font-size:14px;color:var(--text);font-weight:300}
.ficon{position:absolute;width:34px;height:34px;border-radius:50%;background:var(--blue);display:flex;align-items:center;justify-content:center}
.ftext{position:absolute;left:773px;font-size:14px;line-height:21px;color:var(--text);font-weight:300}
.social{position:absolute;width:38px;height:38px;border-radius:50%;background:var(--blue)}
</style>
</head>
<body>

<header>
  <div class="abs topbar">
    <span><svg width="14" height="12" viewBox="0 0 14 12" fill="none" stroke="#fff" stroke-width="1.4"><rect x="1" y="1" width="12" height="10" rx="1.5"/><path d="M1 2l6 5 6-5"/></svg>hello@rtmglobal.example</span>
    <span><svg width="12" height="12" viewBox="0 0 24 24" fill="#fff"><path d="M6.6 10.8a15 15 0 006.6 6.6l2.2-2.2a1 1 0 011-.25 11.4 11.4 0 003.6.6 1 1 0 011 1V20a1 1 0 01-1 1A17 17 0 013 4a1 1 0 011-1h3.5a1 1 0 011 1c0 1.250.2 2.450.6 3.6a1 1 0 01-.25 1z"/></svg>(034) 7781-3300</span>
    <span class="dots"><span></span><span></span><span></span></span>
  </div>
  <div class="abs brand" style="left:66px;top:30px"><span class="mark"></span><span class="name">RTM Global</span></div>
  <nav class="abs nav"><span class="active">HOME</span><span>ABOUT US</span><span>PRODCUT &amp; SERVICES</span><span>IMPACT</span><span>CONTACT US</span></nav>
</header>

<section class="hero">
  <div class="abs pill"></div>
  <div class="abs avatar" role="img" aria-label="Portrait photo of a smiling farmer"></div>
  <svg class="abs" style="left:413px;top:121px" width="720" height="591" role="img" aria-label="Photo of two farmers carrying fresh vegetables and flowers at a garden market">
    <defs><linearGradient id="heroG" x1="0" y1="0" x2="1" y2="1"><stop offset="0" stop-color="#7d8a62"/><stop offset=".5" stop-color="#556442"/><stop offset="1" stop-color="#3c4a2e"/></linearGradient></defs>
    <path d="M375 0H690Q720 0 720 30V561Q720 591 690 591H30Q0 591 0 561V305Q0 275 30 275H315V30Q315 0 345 0Z" fill="url(#heroG)"/>
  </svg>
  <div class="abs hero-t1">TILLAGE AND</div>
  <div class="abs hero-t2">MEADOWCRAFT</div>
  <h1 class="abs hero-name">RTM Global</h1>
  <p class="abs hero-sub">Revolutionizing Agriculture with Regenerative Solutions</p>
  <div class="btn" style="left:66px;top:607px;width:143px;height:43px">Get Started</div>
</section>

<section class="welcome">
  <div class="abs" style="left:65px;top:817px;width:408px;height:485px;border-radius:50% 50% 46% 46%;background:radial-gradient(circle at 55% 55%,#8b9a6a,#5f6e45 60%,#4d5a39)" role="img" aria-label="Globe and gear illustration with a leaf, framing a farmer in a field"></div>
  <div class="abs eyebrow" style="left:605px;top:860px">Welcome to</div>
  <h2 class="abs h2" style="left:605px;top:884px;width:520px">Rooted Tillage and Meadowcraft</h2>
  <p class="abs para" style="left:605px;top:1017px;width:528px">At RTM, we are committed to reshaping the future of farming through regenerative agriculture. Our solutions go beyond sustainability, actively restoring ecosystems and improving soil health while delivering superior yields. With water-efficient irrigation, innovative agronomy, and a deep focus on soil vitality, we empower farmers to grow more sustainably and profitably.</p>
  <div class="btn" style="left:605px;top:1213px;width:144px;height:44px">Our Mission</div>
</section>

<section class="services">
  <svg class="abs" style="left:66px;top:1411px" width="1067" height="498" role="img" aria-label="Photo of green crop fields under sprinkler irrigation">
    <defs><linearGradient id="fieldG" x1="0" y1="0" x2="0" y2="1"><stop offset="0" stop-color="#5d7048"/><stop offset="1" stop-color="#2f4426"/></linearGradient></defs>
    <path d="M30 0H500L580 147H1037Q1067 147 1067 177V468Q1067 498 1037 498H30Q0 498 0 468V30Q0 0 30 0Z" fill="url(#fieldG)"/>
  </svg>
  <div class="abs" style="left:650px;top:1378px;width:352px;height:500px;border-radius:170px 170px 20px 20px;background:linear-gradient(180deg,#c9b08a,#9aa36a 55%,#3b4d6c)" role="img" aria-label="Photo of a smiling farmer holding a basket of fresh vegetables"></div>
  <h2 class="abs h2" style="left:97px;top:1508px;color:#fff">Our Core<br>Products and Services</h2>

  <svg class="chev" style="left:24px;top:1948px" viewBox="0 0 20 20" fill="none" stroke="#222" stroke-width="2"><path d="M12 4l-6 6 6 6"/></svg>
  <svg class="chev" style="left:1156px;top:1948px" viewBox="0 0 20 20" fill="none" stroke="#222" stroke-width="2"><path d="M8 4l6 6-6 6"/></svg>

  <article class="svc" style="left:78px">
    <div class="icon"><svg width="40" height="40" viewBox="0 0 40 40" fill="none" stroke="#222" stroke-width="1.6"><path d="M6 30h8l8 3 12-6-2-2-9 3h-7"/><path d="M20 22v-8m0 0c-5 0-7-3-7-7 4 0 7 2 7 7zm0 0c0-5 3-7 7-7 0 4-2 7-7 7z"/></svg></div>
    <h3>Regenerative<br>Agricultural Technologies</h3>
    <p>Unlock the future of farming with the latest practices and tools designed to rebuild ecosystems, improve biodiversity, and restore soil carbon levels.</p>
    <div class="btn">Read More</div>
  </article>
  <article class="svc" style="left:434px">
    <div class="icon"><svg width="40" height="40" viewBox="0 0 40 40" fill="none" stroke="#222" stroke-width="1.6"><rect x="10" y="12" width="20" height="8" rx="2"/><path d="M4 10h10M26 10h10M20 20v4M14 28l-2 4M20 28v4M26 28l2 4"/></svg></div>
    <h3>Mobile<br>Drip Irrigation (MDI)</h3>
    <p>Our advanced irrigation system maximizes water use efficiency, reduces waste, and promotes healthier crops.</p>
    <div class="btn">Read More</div>
  </article>
  <article class="svc" style="left:788px">
    <div class="icon"><svg width="40" height="40" viewBox="0 0 40 40" fill="none" stroke="#222" stroke-width="1.6"><rect x="10" y="7" width="20" height="27" rx="2"/><rect x="15" y="4" width="10" height="5" rx="1"/><path d="M14 16h12M14 21h12M14 26h8"/></svg></div>
    <h3>Agronomy Services</h3>
    <p>Unlock the future of farming with the latest practices and tools designed to rebuild ecosystems, improve biodiversity, and restore soil carbon levels.</p>
    <div class="btn">Read More</div>
  </article>
</section>

<section class="why-section">
  <h2 class="abs h2" style="left:0;width:1200px;top:2226px;text-align:center">Why Choose RTM?</h2>
  <svg class="chev" style="left:24px;top:2505px" viewBox="0 0 20 20" fill="none" stroke="#222" stroke-width="2"><path d="M12 4l-6 6 6 6"/></svg>
  <svg class="chev" style="left:1156px;top:2505px" viewBox="0 0 20 20" fill="none" stroke="#222" stroke-width="2"><path d="M8 4l6 6-6 6"/></svg>
  <article class="why" style="left:66px">
    <h3>Champions of<br>Regenerative Agriculture</h3>
    <div class="ph" role="img" aria-label="Photo of a farmer harvesting ripe tomatoes in a greenhouse" style="background:linear-gradient(120deg,#7a8e4a,#b04a2e 55%,#5f7240)"></div>
    <p>We don't just sustain—we regenerate, creating long-term benefits for the environment and your farm.</p>
  </article>
  <article class="why" style="left:427px">
    <h3>Cutting<br>Edge Innovation</h3>
    <div class="ph" role="img" aria-label="Photo of researchers inspecting crops in a greenhouse" style="background:linear-gradient(180deg,#d9dde0,#93b36a 55%,#5e8a3c)"></div>
    <p>Access the latest technologies that promote ecosystem restoration and climate resilience.</p>
  </article>
  <article class="why" style="left:788px">
    <h3>Global Expertise</h3>
    <div class="ph" role="img" aria-label="Photo of two growers tending seedlings at a nursery" style="background:linear-gradient(120deg,#8a8f98,#6aa0a0 50%,#6b7f45)"></div>
    <p>Decades of experience bringing sustainable solutions to diverse farming environments worldwide.</p>
  </article>
</section>

<section class="impact">
  <div class="abs impact-band"></div>
  <div class="abs" style="left:66px;top:2875px;width:539px;height:469px;border-radius:6px;background:linear-gradient(160deg,#6f8a8a,#4b5a3a 60%,#3a3a30)" role="img" aria-label="Photo of a gardener planting seedlings in soil trays"></div>
  <div class="abs" style="left:220px;top:2759px;width:230px;height:160px;border-radius:110px 110px 0 0;background:linear-gradient(180deg,#c9a878,#6f8a8a)" role="img" aria-label="Gardener's head and shoulders rising above the photo frame"></div>
  <h2 class="abs h2" style="left:671px;top:2952px;color:#fff;font-size:48px">Our Impact</h2>
  <p class="abs" style="left:671px;top:3040px;width:470px;font-size:16.5px;line-height:26px;color:#e9e9e2;font-weight:300">We are proud to help farmers build resilient farms, sequester carbon, and regenerate the land. Our approach ensures healthy soils, vibrant ecosystems, and productive crops for generations to come.</p>
  <div class="btn" style="left:671px;top:3166px;width:143px;height:46px">Contact Us</div>
</section>

<section class="contact">
  <svg class="abs" style="left:66px;top:3417px" width="1067" height="520" aria-hidden="true">
    <path d="M30 0H600L660 75H1037Q1067 75 1067 105V520H0V30Q0 0 30 0Z" fill="var(--olive-dark)"/>
  </svg>
  <div class="abs" style="left:640px;top:3365px;width:477px;height:518px;border-radius:150px 150px 10px 10px;background:linear-gradient(180deg,#b98d70,#7b4a4a 55%,#c07a4a)" role="img" aria-label="Photo of a smiling farmer holding a crate of fresh strawberries"></div>
  <h2 class="abs h2" style="left:104px;top:3462px;color:#fff">Get In Touch</h2>
  <p class="abs" style="left:104px;top:3528px;font-size:16px;color:#e7eadb;font-weight:300">Duis aute irure dolor in reprehenderit in voluptate velit...</p>
  <div class="field" style="left:104px;top:3584px;width:236px;height:45px">Name:</div>
  <div class="field" style="left:353px;top:3584px;width:236px;height:45px">Email:</div>
  <div class="field" style="left:104px;top:3642px;width:236px;height:45px">Phone:</div>
  <div class="field" style="left:353px;top:3642px;width:236px;height:104px">Message:</div>
  <div class="btn" style="left:104px;top:3702px;width:236px;height:44px">Send</div>
</section>

<footer class="abs footer">
  <div class="abs brand" style="left:36px;top:52px"><span class="mark"></span><span class="name">RTM Global</span></div>
  <p class="abs" style="left:36px;top:136px;width:330px;font-size:14px;line-height:21px;color:var(--text);font-weight:300">At RTM, we are committed to reshaping the future of farming through regenerative agriculture.</p>
  <span class="social" style="left:36px;top:210px"></span>
  <span class="social" style="left:91px;top:210px"></span>
  <span class="social" style="left:146px;top:210px"></span>

  <h4 style="left:461px;top:30px">Quick Links</h4>
  <span class="link" style="top:76px">Home</span>
  <span class="link" style="top:108px">About Us</span>
  <span class="link" style="top:140px">Product &amp; Services</span>
  <span class="link" style="top:173px">Impact</span>
  <span class="link" style="top:205px">Contact Us</span>

  <h4 style="left:729px;top:30px">Contact Us</h4>
  <div class="ficon" style="left:729px;top:78px"><svg width="14" height="16" viewBox="0 0 14 18" fill="#fff"><path d="M7 0a7 7 0 017 7c0 5-7 11-7 11S0 12 0 7a7 7 0 017-7zm0 4a3 3 0 100 6 3 3 0 000-6z"/></svg></div>
  <p class="ftext" style="top:76px">14 Meadow Lane, Fieldbrook<br>Valley Ridge</p>
  <div class="ficon" style="left:729px;top:142px"><svg width="14" height="14" viewBox="0 0 24 24" fill="#fff"><path d="M6.6 10.8a15 15 0 006.6 6.6l2.2-2.2a1 1 0 011-.25 11.4 11.4 0 003.6.6 1 1 0 011 1V20a1 1 0 01-1 1A17 17 0 013 4a1 1 0 011-1h3.5a1 1 0 011 1c0 1.25.2 2.45.6 3.6a1 1 0 01-.25 1z"/></svg></div>
  <p class="ftext" style="top:149px">+9 (613) 472 5590</p>
  <div class="ficon" style="left:729px;top:196px"><svg width="14" height="12" viewBox="0 0 14 12" fill="none" stroke="#fff" stroke-width="1.5"><rect x="1" y="1" width="12" height="10" rx="1.5"/><path d="M1 2l6 5 6-5"/></svg></div>
  <p class="ftext" style="top:203px">info@rtmglobal.example</p>

  <p class="abs" style="left:0;width:1006px;top:282px;text-align:center;font-size:11px;color:var(--muted)">© <span style="color:var(--olive)">RTM GLOBAL</span>, 2024. ALL RIGHTS RESERVED.</p>
</footer>

</body>
</html>
```